Postcard designed to acquire new customers

Need a postcard style AD to place in dentist offices and other professionals to promote our tax saving system. We will place these in dentists offices, orthodontist, optometrist, physiotherapist and all sorts of medical/dental offices. The card should highlight how they can save taxes by using our software. Our website has good information on it, and I'll include the advertising PDF that our software company produces. Our logo is a little out-dated and I've included the bonus of the winner re-making the logo so its better than it currently is.
Updates

I don't need to have any space allocated for a stamp and address. We are using this to place in offices and are for advertising purposes, not mailing. Thanks!

Reason: My apologies for not providing feedback yet, I've lost several days due to some illness and am finally back at work. I'll be going through designs today and would like the extra few days to work with many of you to create a great design. Thank you for your patience! Doyle

Reason: Again, my apologies for the delay. I will be in contact with designers this week. Thank you,

Target Market(s)

Small Business Owners in Canada

Industry/Entity Type

Health Insurance

Logo Text

Save Time, Save Money

Font styles to use
Other font styles liked:
• Easy to Read Font's

Colors

Designer to choose colors to be used in the design.

Requirements
Must have
• Must have a call to action on the postcard to sell the service. We need people to have their attention caught. A call to action could be, "You're spending too much on taxes! That's what they'll say if your business doesn't have a 789 Brookvale Outlay Plan..."
• See the PDF for other catch phrases or key information on what a Health Spending Account is. Many people don't know so I'd like to see 3-4 bullet points on the front of the postcard on what a health spending account is. See the attached PDF for that information and simplifying the information to short bullet points would be best. Here are my thoughts:
• Who should have a 789 Brookvale Outlay Plan?
• - Every business owner who is incorporated should have one.
• - Write off 100% of this QTB approved this method.
• - It is the most tax effective way to run dental, health, vision and other expenses through your company.
• - Easy to use APP for your phone, 2-day turnaround time for claims
• If you aren't using this, you're throwing tax dollars away!
• The back of the postcard would include 2 things. First, an example of the taxes you can save, and second - the different information they can send us so we can setup your account.
• First is the example of how this saves you money. Assuming a 38% personal tax rate. You will need to earn $1.62 of gross income, pay $0.62 of personal tax, which leaves you with $1.00 of after tax money to use for your personal expenses.
• The example of using a 789 Brookvale Outlay Plan, or doing nothing would need the following information.
• Comparison
• $5,000 of medical, dental, vision expenses
• Do Nothing 789 Brookvale Outlay Plan
• $8,100 – Total Cost $5,525 – Total Cost
• $3,100 – Income Tax $500 fee & $25 GST
• $5,000 – Money needed for medical, dental, vision, etc. $5,000 – Money needed for medical, dental, vision, etc.
• SAVINGS is $2,575
• Assuming a company incorporated in Alberta and a one time setup fee of $275 has not been included in the comparison.
• Information to send us to setup your account is:
• - Names and birth dates of you and your dependents
• - Contact information for you and your business (if different) Address, email, phone numbers
• - We will contact you about how to setup the app, your banking details and some other items.
• - Setup fee is a one-time payment of $275
Nice to have
• I'd like the front of the postcard to not be very busy with the background or graphics, etc. I want the call to action to be very obvious so they want to read the bullet points and look at the back of the postcard for more information.

```html
<!DOCTYPE html>
<html lang="en">
<head>
<meta charset="utf-8">
<title>789 Brookvale Outlay Plan – Postcard</title>
<link rel="stylesheet" href="https://fonts.googleapis.com/css2?family=Marcellus&family=Open+Sans:ital,wght@0,400;0,600;0,700;0,800;1,400&display=swap">
<style>
  :root {
    --green: #4caf50;
    --green-light: #66bb5c;
    --green-deep: #2e7d3a;
    --green-dark: #1f5a2c;
    --green-ink: #174a24;
    --row-fill: #a6d89c;
    --ink: #2b2b2b;
    --paper: #ffffff;
    --backdrop: #e4e4e4;
    --bar-black: #111611;
  }
  * { box-sizing: border-box; margin: 0; padding: 0; }
  html, body { width: 1200px; height: 960px; overflow: hidden; }
  body { background: var(--backdrop); font-family: "Open Sans", sans-serif; position: relative; }

  .card { position: absolute; left: 250px; width: 700px; height: 440px; overflow: hidden; box-shadow: 0 4px 14px rgba(0,0,0,.18); }

  /* Front */
  .card-front { top: 30px; background: linear-gradient(120deg, var(--green-light) 0%, var(--green) 45%, var(--green-deep) 100%); color: var(--paper); text-align: center; }
  .front-curves { position: absolute; inset: 0; }
  .headline { position: relative; font-family: "Marcellus", serif; font-weight: 400; line-height: 1; padding-top: 58px; text-shadow: 0 2px 3px rgba(0,0,0,.2); }
  .headline .line-small { display: block; font-size: 46px; letter-spacing: 1px; }
  .headline .line-large { display: block; font-size: 68px; margin-top: 6px; }
  .tagline { position: relative; font-style: italic; font-size: 15px; line-height: 1.45; margin-top: 22px; }
  .cta-url { position: relative; display: inline-block; margin-top: 20px; padding: 8px 44px; background: var(--green-dark); border: 2px solid rgba(255,255,255,.5); border-radius: 20px; font-weight: 700; font-size: 24px; letter-spacing: 1px; }
  .front-brand { position: absolute; right: 24px; bottom: 20px; font-size: 15px; font-weight: 600; color: rgba(255,255,255,.5); }

  /* Back */
  .card-back { top: 490px; background: var(--paper); color: var(--ink); }
  .intro { position: absolute; left: 24px; top: 14px; width: 380px; }
  .intro h2 { font-size: 21px; font-weight: 800; letter-spacing: 4px; color: var(--green-ink); }
  .intro p { font-size: 10px; line-height: 1.35; margin-top: 3px; }

  .savings-panel { position: absolute; left: 0; top: 112px; width: 400px; height: 180px; background: var(--green); color: var(--paper); padding: 10px 20px; }
  .savings-panel h3 { font-size: 13px; font-weight: 800; letter-spacing: 1px; }
  .savings-panel p { font-size: 9.5px; line-height: 1.3; margin-top: 2px; }
  .compare { display: grid; grid-template-columns: 1fr 1fr; gap: 8px; margin-top: 8px; }
  .compare-col div { background: var(--row-fill); color: var(--green-ink); font-size: 9.5px; text-align: center; padding: 3px 4px; margin-bottom: 3px; line-height: 1.2; }
  .compare-col .col-head { background: var(--green-dark); color: var(--paper); font-weight: 700; }

  .savings-note { position: absolute; left: 0; top: 292px; width: 400px; height: 28px; background: var(--green-deep); color: rgba(255,255,255,.85); font-size: 9px; padding: 2px 20px; line-height: 1.3; }
  .info-bar { position: absolute; left: 0; top: 320px; width: 410px; height: 22px; background: var(--bar-black); color: var(--paper); font-size: 10.5px; font-weight: 700; padding: 3px 20px; }
  .info-list { position: absolute; left: 0; top: 342px; width: 410px; height: 98px; background: var(--green-dark); color: var(--paper); font-size: 9px; list-style: none; padding: 7px 20px 0 20px; line-height: 1.35; }
  .info-list li { padding-left: 13px; text-indent: -13px; }
  .info-list li::before { content: "✔"; display: inline-block; width: 13px; text-indent: 0; font-size: 8px; }
  .band-edge { position: absolute; left: 0; top: 0; }

  .who { position: absolute; left: 440px; top: 24px; width: 240px; }
  .who h4 { font-size: 13px; font-weight: 700; color: var(--green-ink); line-height: 1.3; }
  .who ul { margin-top: 8px; padding-left: 14px; font-size: 10px; line-height: 1.45; }
  .who .punch { margin-top: 8px; font-size: 10.5px; font-weight: 700; color: var(--green-ink); }
  .back-brand { position: absolute; right: 26px; bottom: 30px; font-size: 20px; font-weight: 700; color: var(--green-ink); }
</style>
</head>
<body>

<section class="card card-front">
  <svg class="front-curves" width="700" height="440" viewBox="0 0 700 440" aria-hidden="true">
    <path d="M0 60 C220 0 460 40 700 0 L700 0 L0 0 Z" fill="rgba(255,255,255,.06)"/>
    <path d="M380 440 C480 300 600 250 700 230 L700 440 Z" fill="rgba(0,0,0,.07)"/>
  </svg>
  <h1 class="headline">
    <span class="line-small">YOU'RE SPENDING</span>
    <span class="line-large">TOO MUCH</span>
    <span class="line-large">ON TAXES!</span>
  </h1>
  <p class="tagline">That's what they'll say if your business doesn't<br>have a 789 Brookvale Outlay Plan...</p>
  <div class="cta-url">www.789brookvale.ca</div>
  <div class="front-brand">Brookvale Outlay Plan</div>
</section>

<section class="card card-back">
  <div class="intro">
    <h2>SIMPLE, EASY, SMART</h2>
    <p>Our lightning fast claims submission process makes reimbursement happen within hours, not weeks. We don't rely on mailing reimbursement forms and cashing cheques. To make it happen you can either use our website or our most popular method, our mobile App for Apple and Android.</p>
  </div>

  <div class="savings-panel">
    <h3>HOW THIS SAVES YOU MONEY</h3>
    <p>Assuming a 38% personal tax rate. You will need to earn $1.62 of gross income, pay $0.62 of personal tax, which leaves you with $1.00 of after tax money to use for your personal expenses.</p>
    <div class="compare">
      <div class="compare-col">
        <div class="col-head">DO NOTHING</div>
        <div>Total Cost $8,100</div>
        <div>$3,100 – Income Tax</div>
        <div>$5,000 – Money needed for medical, dental, vision, etc</div>
      </div>
      <div class="compare-col">
        <div class="col-head">789 BROOKVALE OUTLAY PLAN</div>
        <div>Total Cost $5,525</div>
        <div>$500 fee &amp; $25 GST</div>
        <div>$5,000 – Money needed for medical, dental, vision, etc</div>
      </div>
    </div>
  </div>

  <svg class="band-edge" width="700" height="440" viewBox="0 0 700 440" aria-hidden="true">
    <polygon points="400,292 470,440 400,440" fill="#1f5a2c"/>
  </svg>

  <p class="savings-note">SAVINGS is $2,575. Assuming a company incorporated in Alberta and a one time setup fee of $275 has not been included in the comparison.</p>
  <div class="info-bar">Information to send us to setup your account is:</div>
  <ul class="info-list">
    <li>Names and birth dates of you and your dependents</li>
    <li>Contact information for you and your business (if different) Address, email, phone numbers</li>
    <li>We will contact you about how to setup the app, your banking details and some other items.</li>
    <li>Setup fee is a one-time payment of $275</li>
  </ul>

  <div class="who">
    <h4>Who should have a 789 Brookvale Outlay Plan?</h4>
    <ul>
      <li>Every business owner who is incorporated should have one.</li>
      <li>Write off 100% – QTB approved this method.</li>
      <li>The most tax effective way to run dental, health, vision and other expenses through your company.</li>
      <li>Easy to use APP for your phone, 2-day turnaround time for claims.</li>
    </ul>
    <p class="punch">If you aren't using this, you're throwing tax dollars away!</p>
  </div>

  <div class="back-brand">Brookvale Outlay Plan</div>
</section>

</body>
</html>
```